Glow and Petal med spa needs an awesome eye catching billboard ad

We need a billboard ad design for a Med Spa with location sin Cedarvale and Windermere FL A medical spa where the beauty of nature meets the power of science to treat the whole person, mind, body and soul.

Meadowlight Renewal Med Spa is a medical spa where the beauty of nature meets the power of science to create gorgeous, youthful looking skin. Located in Cedarvale, Florida, but also serving Four Corners, Celebration, and Windermere, Florida, the talented professional team brings decades of experience in world-class skin care to provide holistic, science-backed aesthetic services and health coaching.

Industry/Entity Type

Spa

Colors
fbee3e
fece3e
eea4c8
e667a6
fbee3d

Requirements
Must have
• Locations in Cedarvale and Lake Marlow
Phone 407-555-0192
website www.glowandpetal.example

Boards for each:
Aesthetic Treatments
Cosmetic Injectables
Lumora facial
add color vs too many earthtones, to catch the eye perhaps using yellow, something that catches the eye and stands out from the normal everyday
Thank you!!!!
Nice to have
• Boards for each:
Aesthetic Treatments
Cosmetic Injectables
Lumora facial
add color vs too many earthtones, to catch the eye
photos that match services,
Thank you!!!!

```html
<!DOCTYPE html>
<html lang="en">
<head>
<meta charset="utf-8">
<title>Lumora Facial Banner – Meadowlight Renewal Med Spa</title>
<link rel="stylesheet" href="https://fonts.googleapis.com/css2?family=Cinzel:wght@400;700&family=Montserrat:wght@600&display=swap">
<style>
  :root {
    --stage: #ecebea;
    --banner: #ffffff;
    --pink: #e667a6;
    --yellow: #fbd33e;
    --ink: #4f4f52;
    --gold: #c8ac74;
    --photo-warm: #f3dcc4;
    --photo-deep: #b98a6c;
    --photo-sky: #fbf4ec;
  }
  * { margin: 0; padding: 0; box-sizing: border-box; }
  html, body {
    width: 1200px;
    height: 814px;
    overflow: hidden;
    background: var(--stage);
  }
  .banner {
    position: absolute;
    left: 0;
    top: 256px;
    width: 1200px;
    height: 302px;
    background: var(--banner);
    overflow: hidden;
  }
  .hero-photo {
    position: absolute;
    left: 676px;
    top: 0;
    width: 524px;
    height: 302px;
    background:
      radial-gradient(ellipse 120px 160px at 230px 160px, var(--photo-deep) 0%, rgba(185,138,108,0.55) 55%, rgba(243,220,196,0) 100%),
      linear-gradient(180deg, var(--photo-sky) 0%, var(--photo-warm) 60%, var(--photo-sky) 100%);
    -webkit-mask-image: linear-gradient(90deg, transparent 0%, #000 28%, #000 100%), linear-gradient(0deg, transparent 0%, #000 22%);
    -webkit-mask-composite: source-in;
    mask-image: linear-gradient(90deg, transparent 0%, #000 28%, #000 100%), linear-gradient(0deg, transparent 0%, #000 22%);
    mask-composite: intersect;
  }
  .headline {
    position: absolute;
    right: 467px;
    top: 84px;
    font-family: "Cinzel", serif;
    font-weight: 700;
    font-size: 52px;
    line-height: 1;
    color: var(--pink);
    white-space: nowrap;
  }
  .locations {
    position: absolute;
    left: 373px;
    top: 150px;
    width: 361px;
    height: 30px;
    background: var(--yellow);
    font-family: "Montserrat", sans-serif;
    font-weight: 600;
    font-size: 19px;
    line-height: 30px;
    color: var(--ink);
    text-align: right;
    padding-right: 14px;
    white-space: nowrap;
  }
  .contact {
    position: absolute;
    right: 471px;
    top: 204px;
    text-align: right;
    font-family: "Montserrat", sans-serif;
    font-weight: 600;
    color: var(--ink);
    white-space: nowrap;
  }
  .contact .phone { font-size: 31px; line-height: 36px; }
  .contact .web { font-size: 14px; line-height: 20px; letter-spacing: 0.2px; }
  .spa-name {
    position: absolute;
    left: 52px;
    top: 214px;
    font-family: "Cinzel", serif;
    font-weight: 400;
    font-size: 19px;
    line-height: 26px;
    letter-spacing: 2px;
    color: var(--gold);
    white-space: nowrap;
  }
</style>
</head>
<body>
  <main class="banner">
    <div class="hero-photo" role="img" aria-label="Photo of a woman in a straw hat with a sunlit seaside town behind her"></div>
    <h1 class="headline">Lumora facial</h1>
    <p class="locations">CEDARVALE AND LAKE MARLOW</p>
    <div class="contact">
      <p class="phone">407-555-0192</p>
      <p class="web">WWW.GLOWANDPETAL.EXAMPLE</p>
    </div>
    <p class="spa-name">Meadowlight<br>Renewal Med Spa</p>
  </main>
</body>
</html>
```